professional business card

Professional business card with logo on one side, and underneath logo list:
- power
-data
-fibre optic
-isolar

On other side:
Marcus Webb
Owner
MOB 0432 958 720
marcus@vorn.com.au
www.vornelectrical.com.au

Please edit logo to just leave VORN

```html
<!DOCTYPE html>
<html lang="en">
<head>
<meta charset="utf-8">
<title>VORN Electrical – Business Card</title>
<link href="https://fonts.googleapis.com/css2?family=Fira+Sans:wght@300;400;700&display=swap" rel="stylesheet">
<style>
  :root {
    --backdrop: #7e3a1e;
    --navy: #1c1b4a;
    --mid: #2f4a62;
    --teal: #5a9692;
    --line: #a9d6de;
    --dot: #ffffff;
    --text-light: #a9d4dc;
  }
  * { margin: 0; padding: 0; box-sizing: border-box; }
  html, body {
    width: 1200px; height: 1200px; overflow: hidden;
    background: var(--backdrop);
    font-family: "Fira Sans", sans-serif;
  }
  .stage {
    width: 1200px; height: 1200px;
    display: flex; flex-direction: column; align-items: center; justify-content: center;
    gap: 60px;
  }
  .card {
    position: relative;
    width: 900px; height: 514px;
    background: linear-gradient(to bottom, var(--navy) 0%, var(--mid) 50%, var(--teal) 100%);
    box-shadow: 0 10px 24px rgba(0,0,0,0.35);
    overflow: hidden;
  }
  .card-lines { position: absolute; inset: 0; width: 100%; height: 100%; }
  .card-lines line { stroke: var(--line); stroke-width: 3; }
  .card-lines circle { fill: var(--dot); }

  /* front */
  .brand-name {
    position: absolute; left: 0; right: 0; top: 150px;
    text-align: center;
    font-weight: 400; font-size: 96px; letter-spacing: 0.2em;
    padding-left: 0.2em;
    color: var(--text-light); line-height: 1;
  }
  .services {
    position: absolute; left: 100px; top: 398px;
    display: flex; align-items: center; gap: 26px;
    font-size: 35px; font-weight: 400; letter-spacing: 0.08em;
    color: var(--text-light);
  }
  .services .sep {
    width: 11px; height: 11px; border: 2px solid var(--text-light); border-radius: 50%;
  }

  /* back */
  .person { position: absolute; left: 100px; top: 92px; color: var(--text-light); }
  .person-name { font-size: 36px; font-weight: 700; letter-spacing: 0.17em; line-height: 1.1; }
  .person-role { font-size: 31px; font-weight: 300; letter-spacing: 0.2em; margin-top: 4px; }
  .contacts {
    position: absolute; left: 370px; top: 276px;
    list-style: none; color: var(--text-light);
    font-size: 23px; font-weight: 400; letter-spacing: 0.16em;
  }
  .contacts li { display: flex; align-items: center; gap: 20px; height: 50px; }
  .contacts svg { width: 34px; height: 34px; flex: none; }
  .contacts .phone { font-size: 27px; }
</style>
</head>
<body>
<main class="stage">
  <section class="card card-front">
    <svg class="card-lines" viewBox="0 0 900 514" aria-hidden="true">
      <line x1="0" y1="370" x2="900" y2="370"/>
      <circle cx="100" cy="370" r="8"/>
      <circle cx="450" cy="370" r="8"/>
      <circle cx="800" cy="370" r="8"/>
    </svg>
    <h1 class="brand-name">VORN</h1>
    <p class="services">
      <span>power</span><span class="sep"></span>
      <span>data</span><span class="sep"></span>
      <span>fibre optic</span><span class="sep"></span>
      <span>isolar</span>
    </p>
  </section>

  <section class="card card-back">
    <svg class="card-lines" viewBox="0 0 900 514" aria-hidden="true">
      <line x1="0" y1="194" x2="900" y2="194"/>
      <circle cx="100" cy="194" r="8"/>
      <circle cx="450" cy="194" r="8"/>
      <circle cx="800" cy="194" r="8"/>
      <line x1="0" y1="444" x2="900" y2="444"/>
      <circle cx="100" cy="444" r="8"/>
      <circle cx="450" cy="444" r="8"/>
      <circle cx="800" cy="444" r="8"/>
    </svg>
    <div class="person">
      <h2 class="person-name">MARCUS WEBB</h2>
      <p class="person-role">OWNER</p>
    </div>
    <ul class="contacts">
      <li class="phone">
        <svg viewBox="0 0 34 34" aria-hidden="true"><rect x="9" y="2" width="16" height="30" rx="3" fill="none" stroke="var(--text-light)" stroke-width="2.5"/><circle cx="17" cy="27" r="1.8" fill="var(--text-light)"/></svg>
        <span>0432 958 720</span>
      </li>
      <li>
        <svg viewBox="0 0 34 34" aria-hidden="true"><rect x="2" y="8" width="30" height="20" fill="var(--text-light)"/><polyline points="2,8 17,20 32,8" fill="none" stroke="var(--mid)" stroke-width="2"/></svg>
        <span>marcus@vorn.com.au</span>
      </li>
      <li>
        <svg viewBox="0 0 34 34" aria-hidden="true" fill="none" stroke="var(--text-light)" stroke-width="2"><circle cx="17" cy="17" r="14"/><ellipse cx="17" cy="17" rx="6" ry="14"/><line x1="3" y1="17" x2="31" y2="17"/><line x1="17" y1="3" x2="17" y2="31"/></svg>
        <span>www.vornelectrical.com.au</span>
      </li>
    </ul>
  </section>
</main>
</body>
</html>
```